Detailed services rate card

We need a detailed rate card to promote our services to our customers.
The information is in the Word document dealrack-Rates-2015. Our customers are businesses that want to advertise their sales on our websites (http://www.dealrack-example.ca & http://www.lesrabais-example.ca

We would like a colorful but professional rate card. Please see our other rate card (dealrack-premium-2015-packages). The detailed rate card should have a design that fits this other rate card we are using.

```html
<!DOCTYPE html>
<html lang="en">
<head>
<meta charset="utf-8">
<title>dealrack.ca – 2015 Rates</title>
<link rel="stylesheet" href="https://fonts.googleapis.com/css2?family=Open+Sans:wght@400;600;700&family=Lato:wght@700;900&display=swap">
<style>
:root{
  --magenta:#e3196f;
  --pink-deep:#ec5c9c;
  --pink-soft:#f7b3d2;
  --pink-pale:#fde3ef;
  --cell:#ffffff;
  --cell-line:#f1c6da;
  --ink:#2a2a2a;
  --gold:#fbb615;
  --gold-pale:#fff1c8;
  --heading-ink:#7a2a12;
}
*{box-sizing:border-box;margin:0;padding:0}
html,body{width:848px;height:1200px;overflow:hidden}
body{font-family:"Open Sans",Arial,sans-serif;color:var(--ink);background:#fff}
.sheet{position:relative;width:848px;height:1200px;overflow:hidden;
  background:linear-gradient(180deg,#fff 0,#fff 60px,var(--pink-soft) 130px,var(--pink-deep) 175px,#f28bb8 600px,#f6a9cb 1200px)}
.backdrop{position:absolute;inset:0;
  background:radial-gradient(circle at 12% 78%,rgba(255,214,120,.45) 0,transparent 22%),
             radial-gradient(circle at 90% 40%,rgba(255,255,255,.35) 0,transparent 25%),
             radial-gradient(circle at 30% 20%,rgba(255,200,230,.5) 0,transparent 30%)}
.brand{position:absolute;left:26px;top:26px;display:flex;align-items:center;gap:10px}
.brand-name{font-family:"Lato",Arial,sans-serif;font-weight:900;font-size:54px;color:var(--magenta);letter-spacing:-1px}
.brand-dot{width:30px;height:30px;border-radius:50%;background:var(--magenta)}
.title{position:absolute;right:24px;top:20px;font-family:"Lato",Arial,sans-serif;font-weight:900;font-size:42px;color:var(--magenta)}
.panel{position:absolute;left:12px;top:166px;width:824px;height:1026px;background:rgba(255,255,255,.35);border:2px solid rgba(255,255,255,.7)}
.grid{position:absolute;left:18px;width:812px;display:grid;grid-template-columns:490px 155px 155px;column-gap:6px}
.grid .label{grid-column:1;background:var(--cell);border:1px solid var(--cell-line);display:flex;align-items:center;padding-left:22px;font-size:22px}
.grid .term,.grid .price{background:var(--cell);border-bottom:2px solid var(--pink-pale);display:flex;align-items:center;justify-content:center;font-size:18px}
.box-one{top:182px;grid-template-rows:repeat(4,30px);row-gap:1px}
.box-two{top:308px;grid-template-rows:repeat(4,30px);row-gap:1px}
.email{top:442px;grid-template-rows:repeat(4,28px);row-gap:2px}
.email .term{font-size:11px}
.email .price{font-size:20px}
.box-one .label,.box-two .label,.email .label{grid-row:1/5}
.section-head{position:absolute;left:18px;width:812px;height:34px;display:grid;grid-template-columns:651px 161px}
.section-head .name{background:var(--gold);display:flex;align-items:center;justify-content:center;font-weight:700;font-size:20px;color:var(--heading-ink)}
.section-head .fill{background:var(--gold-pale)}
.rows{position:absolute;left:18px;width:812px;display:grid;grid-template-columns:651px 161px;background:var(--gold-pale)}
.rows .item,.rows .cost{background:var(--cell);border-bottom:3px solid var(--pink-pale);display:flex;align-items:center}
.rows .item{padding-left:14px;font-size:12.5px;line-height:1.35}
.rows .cost{justify-content:center;text-align:center;font-size:20px;border-left:6px solid var(--gold-pale)}
.rows .cost small{display:block;font-size:14px;line-height:1.2}
.other-head{top:569px}
.services{top:603px;grid-auto-rows:50px}
.long-head{top:955px}
.agreements{top:990px;grid-auto-rows:48px}
.agreements .cost{font-size:15px;line-height:1.2;flex-direction:column}
.design-head{top:1092px}
.design{top:1128px;grid-auto-rows:56px}
</style>
</head>
<body>
<main class="sheet">
  <div class="backdrop" role="img" aria-label="Soft pink and gold light bokeh background"></div>

  <header>
    <div class="brand"><span class="brand-name">dealrack.ca</span><span class="brand-dot"></span></div>
    <h1 class="title">2015 RATES*</h1>
  </header>

  <div class="panel"></div>

  <section class="grid box-one">
    <div class="label">Big box #1</div>
    <div class="term">1 week</div><div class="price">$150</div>
    <div class="term">2 week</div><div class="price">$200</div>
    <div class="term">3 week</div><div class="price">$275</div>
    <div class="term">4 week</div><div class="price">$325</div>
  </section>

  <section class="grid box-two">
    <div class="label">Big box #2 &amp; #3</div>
    <div class="term">1 week</div><div class="price">$125</div>
    <div class="term">2 week</div><div class="price">$175</div>
    <div class="term">3 week</div><div class="price">$250</div>
    <div class="term">4 week</div><div class="price">$300</div>
  </section>

  <section class="grid email">
    <div class="label">Targeted email advertising</div>
    <div class="term">10,000 to 14,999 emails</div><div class="price">$40 CPM</div>
    <div class="term">15,000 to 19,999 emails</div><div class="price">$35 CPM</div>
    <div class="term">20,000 to 24,999 emails</div><div class="price">$30 CPM</div>
    <div class="term">25,000+ emails</div><div class="price">$25 CPM</div>
  </section>

  <div class="section-head other-head"><div class="name">Other services</div><div class="fill"></div></div>
  <section class="rows services">
    <div class="item">VIP Sale(Your visual will appear at the top our newsletter, and 1 post Circlebook/Chirply)</div><div class="cost">$50</div>
    <div class="item">dealrack.ca Squad:coverage of your sale on Chirply and Circlebook</div><div class="cost">$300 per day</div>
    <div class="item">Sponsored blog post on dealrack.ca’s blog</div><div class="cost">$150</div>
    <div class="item">Video of your sale or store (posted only on dealrack-example.ca/lesrabais-example.ca’s website)</div><div class="cost">$300</div>
    <div class="item">Video of your sale or store (Video file provided and copyrights to use as you wish)</div><div class="cost">$400</div>
    <div class="item">Professional photo shoot (combined with a filming shoot)</div><div class="cost">$100</div>
    <div class="item">Professional photo shoot</div><div class="cost">$200</div>
  </section>

  <div class="section-head long-head"><div class="name">Long-term agreements</div><div class="fill"></div></div>
  <section class="rows agreements">
    <div class="item">6 months: you pay the first 5 months and the 6th month is free.<br>Payable in 3 instalments.</div><div class="cost">$725<small>($120.83/month)</small></div>
    <div class="item">12 months: get a 20% discount and save $350.<br>Payable in 3 instalments.</div><div class="cost">$1,390<small>($115.83/month)</small></div>
  </section>

  <div class="section-head design-head"><div class="name">Graphic design</div><div class="fill"></div></div>
  <section class="rows design">
    <div class="item">Graphic design - flyer / small photo / big box or other. The price varies<br>depending on the complexity of the work (ex: photo editing, visual research, etc.).</div><div class="cost">$50 - $200</div>
  </section>
</main>
</body>
</html>
```